TORVEL Business Card Design

We need a business card design for a current Plastering company now moving to building and constructing new homes.
We have been in the Plastering(rendering) business for 15yrs and have made a good name with our customers for our Top Quality of work that we provide.
We would like TORVEL to be the main attraction with an image of architectural roof tops or house design within it. Blue Yellow and Black are colours we like but are willing to see other ideas.
We would like the design to be modern and communicate quality and experience.
Industry/Entity Type
Building
Contact Information for Business Card
TORVEL Building and Plastering
PO BOX 57390 Marlowe Darwin NT 0815
PH/Fax: 08 89317725 Email: torvel@quellnet.com
Dale: 0417396248 Rosa:0409273516
ABN:58 297 130 846

```html
<!DOCTYPE html>
<html lang="en">
<head>
<meta charset="utf-8">
<title>TORVEL Building and Plastering – Business Card</title>
<link rel="stylesheet" href="https://fonts.googleapis.com/css2?family=Didact+Gothic&display=swap">
<style>
  :root {
    --paper-top: #e4e4e4;
    --paper-bottom: #ffffff;
    --band-dark: #0d3f8f;
    --band-light: #4a86cf;
    --motif-blue: #2a62b4;
    --ink-dark: #1a1a1a;
    --panel-top: #1c1c1c;
    --panel-bottom: #0c0c0c;
    --accent-yellow: #f2de1c;
    --text-light: #ffffff;
  }
  html, body {
    margin: 0;
    padding: 0;
    width: 1200px;
    height: 741px;
    overflow: hidden;
    background: #ffffff;
  }
  .card {
    position: relative;
    width: 1200px;
    height: 741px;
    overflow: hidden;
    font-family: "Didact Gothic", sans-serif;
  }
  .card__header {
    position: absolute;
    left: 0; top: 0;
    width: 1200px;
    height: 330px;
    background: linear-gradient(to bottom, var(--paper-top), var(--paper-bottom));
  }
  .card__band {
    position: absolute;
    left: 0; top: 330px;
    width: 1200px;
    height: 24px;
    background: linear-gradient(to right, var(--band-dark) 0%, var(--band-dark) 30%, var(--band-light) 65%, var(--band-dark) 100%);
  }
  .card__panel {
    position: absolute;
    left: 0; top: 354px;
    width: 1200px;
    height: 387px;
    background: linear-gradient(to bottom, var(--panel-top), var(--panel-bottom));
  }
  .brand__motif {
    position: absolute;
    left: 46px;
    top: 70px;
    width: 672px;
    height: 76px;
    background: linear-gradient(to bottom, rgba(42, 98, 180, 0.28), rgba(42, 98, 180, 0.06));
  }
  .brand__name {
    position: absolute;
    left: 118px;
    top: 128px;
    margin: 0;
    font-size: 156px;
    line-height: 1;
    font-weight: 400;
    letter-spacing: 15px;
    color: var(--ink-dark);
  }
  .brand__tagline {
    position: absolute;
    left: 104px;
    top: 270px;
    margin: 0;
    font-size: 55px;
    line-height: 1;
    font-weight: 400;
    letter-spacing: 1px;
    color: var(--accent-yellow);
  }
  .contact {
    position: absolute;
    left: 71px;
    top: 364px;
    margin: 0;
    font-size: 34px;
    line-height: 43.5px;
    color: var(--text-light);
  }
  .contact__row {
    display: flex;
    margin: 0;
  }
  .contact__label {
    width: 113px;
    color: var(--accent-yellow);
  }
  .contact__sep {
    width: 21px;
    color: var(--accent-yellow);
  }
  .contact__address {
    margin: 0 0 0 134px;
    font-size: 37px;
  }
  .contact__abn {
    margin: 2px 0 0 136px;
    font-size: 30px;
  }
</style>
</head>
<body>
  <main class="card">
    <div class="card__header"></div>
    <div class="card__band"></div>
    <div class="card__panel"></div>

    <div class="brand__motif" role="img" aria-label="Space for a house roof outline motif above the company name"></div>
    <h1 class="brand__name">TORVEL</h1>
    <p class="brand__tagline">Building and Plastering</p>

    <div class="contact">
      <p class="contact__row"><span class="contact__label">Ph/Fax</span><span class="contact__sep">:</span><span>08 89317725</span></p>
      <p class="contact__row"><span class="contact__label">Dale</span><span class="contact__sep">:</span><span>0417396248</span></p>
      <p class="contact__row"><span class="contact__label">Rosa</span><span class="contact__sep">:</span><span>0409273516</span></p>
      <p class="contact__row"><span class="contact__label">Email</span><span class="contact__sep">:</span><span>torvel@quellnet.com</span></p>
      <p class="contact__row"><span class="contact__label">Web</span><span class="contact__sep">:</span><span>www.torvel.com.au</span></p>
      <p class="contact__address">PO BOX 57390 Marlowe Darwin NT 0815</p>
      <p class="contact__abn">ABN:58 297 130 846</p>
    </div>
  </main>
</body>
</html>
```